Book cover design, title is "Go Solo Now: How to Swap Your Salary in 10 Seasons"

Design a cover for a book about freelancing. Example of my previous book's cover attached. Book title is "Go Solo Now: How to Swap Your Salary in 10 Seasons". Looking to target people who have a 9-5 job but are seeking to try out freelancing as a way to supplement income and eventually quit their day job.

Target Market(s)

Looking to target people who have a 9-5 job but are seeking to try out freelancing as a way to supplement income and eventually quit their day job.

Industry/Entity Type

Consulting

Font styles to use
Serif
Sans Serif

Colors

Designer to choose colors to be used in the design.

Requirements
Must have
• I love these books covers...
• https://www.pagelodge.example/Tame-Notebin-Casual-Sorting-Settled-ebook/dp/Q71MWRTZPA/ref=asap_bc?ie=UTF8
• https://www.pagelodge.example/Bright-Dawn-Scribes-Drafting-Doubles/dp/5830617294/ref=asap_bc?ie=UTF8
• https://www.pagelodge.example/Way-Pen-Factual-eBook-Weeks-ebook/dp/Q93KT41ZXN/ref=asap_bc?ie=UTF8
• https://www.pagelodge.example/Ritual-Piling-Tiny-Shifts-Moments/dp/6027158392/ref=asap_bc?ie=UTF8
• https://www.pagelodge.example/Boost-Each-Hour-Core-ebook/dp/Q82WFN6JTM/ref=asap_bc?ie=UTF8
• https://www.pagelodge.example/Artisan-Co-Total-Thriving-Gig-ebook/dp/Q66813XKVR/ref=sr_1_4?ie=UTF8&qid=2738405519&sr=8-4&keywords=freelancing
Should not have
• Don't submit 3D renderings, just the front cover image please.

```html
<!DOCTYPE html>
<html lang="en">
<head>
<meta charset="utf-8">
<title>Go Solo Now – Book Cover</title>
<link href="https://fonts.googleapis.com/css2?family=Passion+One:wght@700&family=Fredoka:wght@600&family=Fjalla+One&family=Oswald:wght@500&display=swap" rel="stylesheet">
<style>
  :root {
    --page: #ffffff;
    --photo-top: #7d5a3e;
    --photo-mid: #8e8178;
    --photo-low: #4f5e62;
    --teal: #1f6f80;
    --teal-dark: #175868;
    --orange: #f7941d;
    --white: #ffffff;
    --navy: #173a55;
    --ink: #1d4f5e;
    --grey-light: #b9b6b3;
    --grey-mid: #9a9795;
    --grey-dark: #4a4a4c;
    --series: #c9d3dc;
  }
  html, body {
    margin: 0;
    width: 1200px;
    height: 1200px;
    overflow: hidden;
    background: var(--page);
  }
  .cover {
    position: absolute;
    left: 186px;
    top: 50px;
    width: 828px;
    height: 1100px;
    overflow: hidden;
    background: var(--photo-low);
  }
  .cover-photo {
    position: absolute;
    inset: 0 0 314px 0;
    background: linear-gradient(180deg, var(--photo-top) 0%, var(--photo-mid) 55%, var(--photo-low) 100%);
  }
  .title-band {
    position: absolute;
    left: 0;
    top: 0;
    width: 828px;
    height: 1100px;
  }
  .title {
    position: absolute;
    left: 30px;
    top: 420px;
    margin: 0;
    font-family: "Passion One", "Arial Black", sans-serif;
    font-weight: 700;
    text-transform: uppercase;
    line-height: 0.82;
    transform: rotate(-6deg);
    transform-origin: left top;
  }
  .title-line { display: block; font-size: 168px; }
  .title-line--white { color: var(--white); }
  .title-line--orange { color: var(--orange); margin-left: 74px; }
  .subtitle-band {
    position: absolute;
    left: 0;
    top: 786px;
    width: 828px;
    height: 176px;
    background: linear-gradient(180deg, var(--grey-mid) 0%, var(--grey-light) 40%, #b3b0ad 100%);
  }
  .subtitle {
    position: absolute;
    left: 104px;
    top: 822px;
    margin: 0;
    font-family: "Fredoka", "Arial Rounded MT Bold", sans-serif;
    font-weight: 600;
    font-size: 62px;
    line-height: 67px;
    letter-spacing: -1.5px;
    color: var(--ink);
  }
  .subtitle .accent { color: var(--white); }
  .footer-band {
    position: absolute;
    left: 0;
    top: 962px;
    width: 828px;
    height: 138px;
    background: linear-gradient(180deg, #8f8c8a 0%, #6b696a 45%, var(--grey-dark) 100%);
  }
  .series {
    position: absolute;
    left: 54px;
    top: 984px;
    width: 240px;
    height: 76px;
    display: flex;
    align-items: center;
    gap: 10px;
  }
  .series-mark {
    width: 22px;
    height: 22px;
    background: var(--navy);
    flex: none;
  }
  .series-name {
    font-family: "Oswald", sans-serif;
    font-weight: 500;
    font-size: 24px;
    line-height: 1.05;
    text-transform: uppercase;
    color: var(--series);
  }
  .author {
    position: absolute;
    left: 317px;
    top: 990px;
    margin: 0;
    font-family: "Fjalla One", "Impact", sans-serif;
    font-size: 76px;
    line-height: 1;
    color: var(--orange);
    text-transform: uppercase;
    white-space: nowrap;
  }
</style>
</head>
<body>
  <main class="cover">
    <div class="cover-photo" role="img" aria-label="Photo: a young man with glasses sits on the rim of a giant cappuccino cup, working on a laptop"></div>

    <svg class="title-band" viewBox="0 0 828 1100" aria-hidden="true">
      <path fill="var(--teal)" d="M0 418 L60 412 L130 404 L210 398 L300 390 L390 381 L480 373 L570 364 L660 354 L740 344 L828 334
               L828 612 L740 620 L650 628 L560 636 L470 644 L380 650 L290 656 L200 660 L110 663 L0 666 Z"/>
      <path fill="var(--teal-dark)" opacity="0.35" d="M0 630 L828 578 L828 612 L0 666 Z"/>
    </svg>

    <h1 class="title">
      <span class="title-line title-line--white">Go Solo</span>
      <span class="title-line title-line--orange">Now</span>
    </h1>

    <div class="subtitle-band"></div>
    <p class="subtitle">how to swap your salary<br>in <span class="accent">10 seasons</span></p>

    <div class="footer-band"></div>
    <div class="series">
      <span class="series-mark"></span>
      <span class="series-name">Easygoing Earner<br>Series</span>
    </div>
    <p class="author">Dale Hammond</p>
  </main>
</body>
</html>
```